Tattoostudio
Zielgruppe
Tattoostudio, Junge Leute, Kreativ,
Aufgabenstellung
Visitenkarten mit vorhandenem Logo, hochkant, 2 Seitig, Vorderseite Logo + Studioname (Morgenfalke Tattoo) Rückseite mit Kontaktdaten ( Artist/Inhaber, Facebook: facebook.com/MorgenfalkeTattoo

```html
<!DOCTYPE html>
<html lang="de">
<head>
<meta charset="utf-8">
<title>Morgenfalke Tattoo – Visitenkarten</title>
<link rel="stylesheet" href="https://fonts.googleapis.com/css2?family=Jost:wght@400;600&display=swap">
<style>
  :root {
    --backdrop: #b7bcc8;
    --violet-deep: #4a1f95;
    --violet-mid: #7a6cc0;
    --violet-soft: #a89bd8;
    --slate: #5a5f8e;
    --ink: #000000;
    --logo-grey: #d9d9dc;
    --text-white: #ffffff;
    --illu-pink: #c8407a;
    --illu-teal: #2aa48a;
    --illu-skin: #e9a98f;
  }
  * { box-sizing: border-box; margin: 0; padding: 0; }
  html, body {
    width: 1200px; height: 1200px; overflow: hidden;
    background: var(--backdrop);
    font-family: "Jost", "Futura", sans-serif;
  }
  .canvas { position: relative; width: 1200px; height: 1200px; }

  .card { position: absolute; width: 494px; height: 777px; overflow: hidden; }

  /* Front */
  .card-front {
    left: 83px; top: 89px;
    background: linear-gradient(180deg, var(--slate) 0%, #6f6fae 45%, #2b2b44 72%, var(--ink) 86%);
  }
  .front-illustration {
    position: absolute; left: 0; top: 0; width: 100%; height: 600px;
    background:
      radial-gradient(ellipse 40% 30% at 62% 42%, var(--illu-skin) 0%, rgba(233,169,143,0) 100%),
      radial-gradient(ellipse 55% 25% at 45% 8%, var(--illu-pink) 0%, rgba(200,64,122,0) 100%),
      radial-gradient(ellipse 30% 45% at 20% 45%, var(--illu-teal) 0%, rgba(42,164,138,0) 100%),
      linear-gradient(180deg, #6b5fb0 0%, #5a4c9c 70%, rgba(0,0,0,0) 100%);
  }
  .front-logo {
    position: absolute; left: 0; right: 0; top: 600px;
    text-align: center;
    font-weight: 400; font-size: 54px; line-height: 1.05;
    color: var(--logo-grey); letter-spacing: 1px;
  }

  /* Back */
  .card-back {
    left: 617px; top: 329px;
    background:
      radial-gradient(ellipse 60% 40% at 50% 58%, var(--violet-soft) 0%, rgba(168,155,216,0) 100%),
      linear-gradient(180deg, #6e63a8 0%, var(--violet-mid) 55%, var(--violet-deep) 100%);
  }
  .back-illustration {
    position: absolute; left: 0; top: 0; width: 100%; height: 480px; opacity: 0.35;
    background:
      radial-gradient(ellipse 40% 30% at 62% 55%, var(--illu-skin) 0%, rgba(233,169,143,0) 100%),
      radial-gradient(ellipse 55% 22% at 50% 6%, var(--illu-pink) 0%, rgba(200,64,122,0) 100%),
      radial-gradient(ellipse 30% 40% at 25% 40%, var(--illu-teal) 0%, rgba(42,164,138,0) 100%);
  }
  .contact-list {
    position: absolute; left: 0; right: 0; top: 230px;
    text-align: center; color: var(--text-white);
    text-shadow: 0 1px 3px rgba(0,0,0,0.45);
  }
  .contact-item { margin-bottom: 38px; }
  .contact-label { display: block; font-weight: 600; font-size: 20px; line-height: 1.3; }
  .contact-value { display: block; font-weight: 400; font-size: 22px; line-height: 1.3; letter-spacing: 0.3px; }
</style>
</head>
<body>
<main class="canvas">
  <section class="card card-front" aria-label="Vorderseite">
    <div class="front-illustration" role="img" aria-label="Illustration: Tattoo-Künstlerin im Comic-Stil mit bunten Haaren, Blume und Tätowiermaschine"></div>
    <p class="front-logo">Morgenfalke<br>Tattoo</p>
  </section>

  <section class="card card-back" aria-label="Rückseite">
    <div class="back-illustration" role="img" aria-label="Blasse Wiederholung der Künstlerinnen-Illustration im Hintergrund"></div>
    <dl class="contact-list">
      <div class="contact-item"><dt class="contact-label">Artist/Inhaber</dt><dd class="contact-value">Lena Korbach</dd></div>
      <div class="contact-item"><dt class="contact-label">Straße</dt><dd class="contact-value">Lindenweg 8</dd></div>
      <div class="contact-item"><dt class="contact-label">Ort</dt><dd class="contact-value">07999 Saalhausen</dd></div>
      <div class="contact-item"><dt class="contact-label">Telefon</dt><dd class="contact-value">0170 / 12 34 567</dd></div>
      <div class="contact-item"><dt class="contact-label">eMail</dt><dd class="contact-value">MorgenfalkeTattoo@beispiel.de</dd></div>
      <div class="contact-item"><dt class="contact-label">Facebook</dt><dd class="contact-value">fb.com/MorgenfalkeTattoo</dd></div>
    </dl>
  </section>
</main>
</body>
</html>
```